Glow With Mira, Lifting Your Inner Radiance

Selling lipglosses, adding different types of photos with different colours of lip glosses,adding videos etc

Target Market(s)

All

Industry/Entity Type

Beauty industy

Coding

Coded - Design and coding required

Number of Pages Required

4 page

Requirements
Must have
• All payment options,easy to find,clear photos
Nice to have
• Photos of different ethnicity.Black,asian,white women

```html
<!DOCTYPE html>
<html lang="en">
<head>
<meta charset="utf-8">
<title>Glow With Mira</title>
<link href="https://fonts.googleapis.com/css2?family=Playfair+Display:wght@400;600;700&family=Montserrat:wght@400;500;600;700&display=swap" rel="stylesheet">
<style>
:root{
  --leaf:#7dc07c;
  --forest:#1f4a22;
  --pine:#2d5a32;
  --coral:#f38b78;
  --accent-red:#e5482f;
  --mint:#c9efc6;
  --mist:#eeeeee;
  --ink:#111;
  --white:#fff;
}
*{box-sizing:border-box;margin:0;padding:0}
html,body{width:1200px;height:3382px;overflow:hidden;background:var(--white);font-family:"Montserrat",sans-serif;color:var(--ink)}
.page{position:relative;width:1200px;height:3382px}
.abs{position:absolute}
.serif{font-family:"Playfair Display",serif}

/* header */
.site-header{position:absolute;left:0;top:0;width:1200px;height:82px;background:var(--white);z-index:3}
.brand{position:absolute;left:142px;top:14px;display:flex;flex-direction:column;align-items:center;gap:6px}
.brand-name{font-family:"Playfair Display",serif;font-weight:700;font-size:13px;letter-spacing:2.5px;color:var(--forest);text-transform:uppercase}
.brand-dot{width:90px;height:90px;border-radius:50%;background:var(--forest);border:6px solid var(--white)}
.nav{position:absolute;top:17px;left:567px;display:flex;align-items:center;font-family:"Playfair Display",serif;font-size:18px;color:#333}
.nav a{color:inherit;text-decoration:none;height:46px;line-height:46px;padding:0 16px;margin-right:8px}
.nav a.active{background:var(--forest);color:var(--white);border-radius:23px;padding:0 17px}

/* hero */
.hero{position:absolute;left:0;top:82px;width:1200px;height:554px;background:var(--leaf);overflow:hidden}
.hero svg{position:absolute;left:0;top:0}
.hero-copy{position:absolute;left:723px;top:222px}
.hero-title{font-family:"Playfair Display",serif;font-weight:700;font-size:46px;line-height:52px;color:var(--forest);letter-spacing:1px}
.hero-sub{font-size:22px;color:var(--forest);margin-top:10px;margin-left:3px}
.btn-pill{display:inline-block;background:var(--white);color:var(--ink);font-weight:700;font-size:14px;height:38px;line-height:38px;padding:0 22px;border-radius:19px;margin-top:20px}
.dots{position:absolute;left:733px;top:465px;display:flex;gap:8px}
.dots span{width:18px;height:3px;background:var(--forest)}
.dots span.on{background:var(--white)}

/* welcome */
.eyebrow{left:0;width:1200px;text-align:center;font-size:17px;top:678px}
.section-title{left:0;width:1200px;text-align:center;font-family:"Playfair Display",serif;font-weight:700;font-size:45px;color:var(--forest);letter-spacing:1px}
.intro{left:180px;width:824px;top:760px;text-align:center;font-size:13.5px;line-height:19px}
.video-main{left:228px;top:853px;width:744px;height:389px;border-radius:22px;background:linear-gradient(180deg,#3a3431,#5a3f35 60%,#a55040)}
.play{position:absolute;width:48px;height:48px;border-radius:50%;background:var(--white)}
.play::after{content:"";position:absolute;left:19px;top:14px;border-left:15px solid #111;border-top:10px solid transparent;border-bottom:10px solid transparent}

/* products */
.tabs{left:0;width:1200px;top:1349px;text-align:center;font-size:15px;font-weight:600}
.tabs span{margin:0 7px}
.tabs .current{color:var(--accent-red);font-weight:500}
.note{left:210px;width:780px;top:1391px;text-align:center;font-size:13.5px;line-height:18px}
.card{position:absolute;top:1480px;width:210px;height:315px;border-radius:12px;background:var(--leaf)}
.card.coral{background:var(--coral)}
.card-img{position:absolute;left:11px;top:11px;width:188px;height:239px;border-radius:8px}
.card-label{position:absolute;left:18px;top:270px;font-family:"Playfair Display",serif;font-weight:700;font-size:14px;color:var(--white);letter-spacing:.5px}
.chev{position:absolute;width:12px;height:12px;border-left:2.5px solid #666;border-bottom:2.5px solid #666}

/* videos band */
.videos{left:0;top:1879px;width:1200px;height:688px;background:var(--pine)}
.videos .section-title{color:var(--white);top:62px}
.thumb{position:absolute;top:163px;height:278px}
.videos h3{position:absolute;left:0;width:1200px;top:480px;text-align:center;font-family:"Playfair Display",serif;font-weight:600;font-size:24px;color:var(--white)}
.videos p{position:absolute;left:220px;width:760px;top:528px;text-align:center;font-size:18px;line-height:23px;color:var(--white)}

/* newsletter */
.newsletter{left:0;top:2567px;width:1200px;height:463px;background:var(--mist)}
.newsletter h2{position:absolute;left:0;width:1200px;top:115px;text-align:center;font-family:"Playfair Display",serif;font-weight:600;font-size:41px;line-height:47px;color:var(--forest)}
.signup{position:absolute;left:335px;top:295px;width:532px;height:53px;border-radius:27px;background:var(--white)}
.signup span{position:absolute;left:22px;top:17px;font-size:15px;color:#333}
.signup b{position:absolute;right:8px;top:7px;height:39px;line-height:39px;padding:0 22px;border-radius:20px;background:var(--mint);font-size:15px;font-weight:700}

/* footer */
.footer{left:0;top:3030px;width:1200px;height:352px;background:linear-gradient(90deg,#24472a,#2f5a31 50%,#24472a)}
.foot-brand{position:absolute;left:0;width:1200px;top:55px;display:flex;flex-direction:column;align-items:center;gap:8px}
.foot-brand .brand-name{color:var(--white)}
.foot-brand i{width:70px;height:70px;border-radius:50%;background:var(--white)}
.foot-links{position:absolute;left:0;width:1200px;top:182px;text-align:center;font-size:14px;color:var(--white)}
.foot-links span{margin:0 12px}
.socials{position:absolute;left:493px;top:233px;display:flex;gap:13px}
.socials i{width:44px;height:44px;border-radius:50%;background:var(--mint)}
.copy{position:absolute;left:0;width:1200px;top:298px;text-align:center;font-size:13.5px;color:var(--white)}
</style>
</head>
<body>
<div class="page">

<header class="site-header">
  <div class="brand"><span class="brand-name">Glow With Mira</span><span class="brand-dot"></span></div>
  <nav class="nav"><a class="active">Home</a><a>About</a><a>Products</a><a>Shop</a><a>Contact Us</a></nav>
</header>

<section class="hero">
  <svg width="1200" height="554" viewBox="0 82 1200 554">
    <polygon points="500,82 818,82 460,636 0,636 0,590" fill="var(--forest)"/>
    <polygon points="430,82 712,82 458,636 100,636" fill="#8a5a48" role="img" aria-label="Photo of a model holding a coral lip gloss"/>
  </svg>
  <div class="hero-copy">
    <div class="hero-title">ENHANCING<br>BEAUTY</div>
    <div class="hero-sub">One Gloss at a Time</div>
    <div class="btn-pill">VIEW OUR PRODUCTS</div>
  </div>
  <div class="dots"><span></span><span class="on"></span><span></span><span></span><span></span></div>
</section>

<div class="abs eyebrow">WELCOME</div>
<h1 class="abs section-title" style="top:700px">MY BEAUTY JOURNEY</h1>
<p class="abs intro">Step into a world where beauty meets confidence. At Glow With Mira, we’re all about helping you feel empowered, radiant, and authentically YOU. Whether you’re new to makeup or a beauty pro, our products are designed to bring out your natural glow and make you feel unstoppable.</p>
<div class="abs video-main" role="img" aria-label="Video still of a model wearing coral lip gloss">
  <span class="play" style="left:348px;top:171px"></span>
</div>

<h2 class="abs section-title" style="top:1268px">PRODUCTS</h2>
<div class="abs tabs"><span class="current">LIP KIT</span> :: <span>LIP GLOSSES</span> :: <span>EPITOME</span> :: <span>SIGNATURE LIP GLOSSES</span></div>
<p class="abs note">lick on the image for a full view and detailed information. Before adding to cart, please ensure you provide your shipping address in the "PROVIDE ORDER OR REQUEST DETAILS" field. All lip glosses are vegan, not tested on animals, and cruelty-free. PRICE INCLUDES SHIPPING</p>

<span class="chev" style="left:76px;top:1600px;transform:rotate(45deg)"></span>
<div class="card" style="left:143px"><div class="card-img" style="background:linear-gradient(160deg,#fff,#e9dde2 60%,#8d3346)" role="img" aria-label="Lip kit 001 with plum gloss"></div><div class="card-label">LIP KIT NO : 001</div></div>
<div class="card coral" style="left:378px"><div class="card-img" style="background:linear-gradient(160deg,#fff,#f4e7e7 55%,#c46b6b)" role="img" aria-label="Lip kit 002 with rose gloss and liner"></div><div class="card-label">LIP KIT NO : 002</div></div>
<div class="card" style="left:613px"><div class="card-img" style="background:linear-gradient(160deg,#fff,#efe4e4 55%,#7a1616)" role="img" aria-label="Lip kit 003 with deep red gloss and liner"></div><div class="card-label">LIP KIT NO : 003</div></div>
<div class="card" style="left:847px"><div class="card-img" style="background:linear-gradient(160deg,#f4f4f4,#b7495a 50%,#5a3a7a)" role="img" aria-label="Lip kit 004 with assorted gloss tubes"></div><div class="card-label">LIP KIT NO : 004</div></div>
<span class="chev" style="left:1106px;top:1597px;transform:rotate(-135deg)"></span>

<section class="abs videos">
  <h2 class="abs section-title">OUR PRODUCT  VIDEOS</h2>
  <div class="thumb" style="left:0;width:202px;background:linear-gradient(135deg,#a01c22,#d9a49a)" role="img" aria-label="Video still of red gloss swatch"></div>
  <div class="thumb" style="left:222px;width:369px;background:linear-gradient(135deg,#3a3a3a,#1a1a1a)" role="img" aria-label="Video still of signature gloss tubes"><span class="play" style="left:160px;top:115px"></span></div>
  <div class="thumb" style="left:610px;width:369px;background:linear-gradient(135deg,#2a1e1b,#6b4436 55%,#b07a62)" role="img" aria-label="Video still of a model applying gloss"><span class="play" style="left:160px;top:115px"></span></div>
  <div class="thumb" style="left:999px;width:201px;background:linear-gradient(135deg,#e6e1da,#8a5a48 60%,#c9453a)" role="img" aria-label="Video still of a model with coral gloss"></div>
  <h3>Where Shine Meets Confidence</h3>
  <p>Explore our signature collection of lip glosses — created to hydrate, glow, and enhance every shade of beauty. Each gloss is made with love and designed to help you feel bold, beautiful, and YOU.</p>
</section>

<section class="abs newsletter">
  <h2>Enjoy a Special 50% New lip glosses<br>are vegan, not tested on animals, and<br>cruelty-free.</h2>
  <div class="signup"><span>Enter your email id</span><b>SUBSCRIBE</b></div>
</section>

<footer class="abs footer">
  <div class="foot-brand"><span class="brand-name">Glow With Mira</span><i></i></div>
  <div class="foot-links"><span>Home</span>.<span>About Us</span>.<span>Products</span>.<span>Shop</span>.<span>Contact Us</span></div>
  <div class="socials"><i></i><i></i><i></i><i></i></div>
  <div class="copy">© 2025 | www.glowwithmira.com</div>
</footer>

</div>
</body>
</html>
```